Label for Whiskey and Rum Bottle

We are a distillery. Whiskey and Rum We like to have a new label for our bottles. The whiskey bottles are in a wooden case. http://www.kornfaesser.ch/store/product/talwinkel-obermatt-single-malt-whiskey-nr-6 The Rum Bottles have no package. The label is even more important. http://www.kornfaesser.ch/store/product/talwinkel-obermatter-rum You can see the form of the bottles here www.kornfaesser.ch/store Whiskey and rum bottles are for a liter (50 cl) The labels can be with a picture or without. We would like to have something completely new. Therefore we don`t like to make much prescriptions concerning the design. We don`t like to give too much information (text) on the label. Just the information required by law. Consumers should understand the labels without long-reading. (The label-text is below) The 2 labels (Whiskey and rum) should look similar. Probably they have a different color or a different picture or .... It should be clear that the 2 products are from the same distillery. We have the intention to change all our existing labels over time. This gives designers the chance for follow-up projects.

Target Market(s)

Adults, liquor lovers

Requirements
Must have
• Information on the label is in German. (See "") Whiskey: - the name of the whiskey is "Talwinkel Obermatt Single Malt Whiskey" - The Whiskey was matured 5 years in a sherry "5 years in the sherry barrel stored" - The Alcohol content is 40% volumes "40% Vol "- The bottle contents 50 cl" 5 dl "- The distillery is" Distillery Brunnacher, Tornwil, www.kornfaesser.ch "- The producer is" Kelvor GmbH "Rum: - The name is" Talwinkel Obermatter Rum "- The alcohol content is 37% Volumes "37% Vol" - The bottle contens 50 cl "5 dl" - The distillery is "Distillery Brunnacher, Tornwil, www.kornfaesser.ch" - The producer is "Kelvor GmbH"
Nice to have
• Premium looking label Only front label preferred Only necessary text on the label
Should not have
• No special print techniques necessary No special paper form

```html
<!DOCTYPE html>
<html lang="de">
<head>
<meta charset="utf-8">
<title>Talwinkel Obermatt – Etikett</title>
<link rel="stylesheet" href="https://fonts.googleapis.com/css2?family=Montserrat:wght@600;700;800&family=Noto+Serif:wght@400;500&display=swap">
<style>
  :root {
    --label-black: #1e1e1d;
    --copper: #b9774a;
    --copper-light: #e0a878;
    --copper-dark: #8a5430;
    --ink-white: #f4f1ec;
  }
  html, body {
    margin: 0;
    width: 1200px;
    height: 1200px;
    overflow: hidden;
  }
  body {
    background: linear-gradient(100deg, #8e8481 0%, #b6aca8 50%, #ddd3cf 100%);
    position: relative;
    font-family: "Noto Serif", serif;
  }
  .label {
    position: absolute;
    left: 100px;
    top: 68px;
    width: 1000px;
    height: 1064px;
    background: var(--label-black);
    color: var(--ink-white);
  }
  .label__frame {
    position: absolute;
    inset: 0;
  }
  .label__distillery {
    position: absolute;
    top: 60px;
    left: 0;
    right: 0;
    text-align: center;
    font-size: 11px;
    letter-spacing: 3px;
    color: var(--copper);
  }
  .label__brand {
    position: absolute;
    top: 160px;
    left: 0;
    right: 0;
    display: flex;
    align-items: center;
    justify-content: center;
    gap: 16px;
    font-family: "Noto Serif", serif;
    font-size: 40px;
    font-weight: 400;
    line-height: 1;
    color: var(--ink-white);
  }
  .label__brand-square {
    width: 22px;
    height: 22px;
    background: var(--ink-white);
  }
  .label__name {
    position: absolute;
    top: 440px;
    left: 0;
    right: 0;
    margin: 0;
    text-align: center;
    font-family: "Montserrat", sans-serif;
    font-weight: 800;
    font-size: 118px;
    letter-spacing: 2px;
    line-height: 1;
    background: linear-gradient(90deg, var(--copper-dark) 0%, var(--copper-light) 30%, var(--copper) 50%, var(--copper-light) 70%, var(--copper-dark) 100%);
    -webkit-background-clip: text;
    background-clip: text;
    color: transparent;
  }
  .label__subname {
    position: absolute;
    top: 596px;
    left: 0;
    right: 0;
    text-align: center;
    font-size: 54px;
    color: var(--copper-light);
  }
  .label__kind {
    position: absolute;
    top: 764px;
    left: 0;
    right: 0;
    text-align: center;
    font-size: 24px;
  }
  .label__producer {
    position: absolute;
    top: 934px;
    left: 0;
    right: 0;
    text-align: center;
    font-size: 18px;
  }
  .label__web {
    position: absolute;
    top: 972px;
    left: 0;
    right: 0;
    text-align: center;
    font-size: 16px;
  }
  .label__fact {
    position: absolute;
    top: 966px;
    font-family: "Montserrat", sans-serif;
    font-weight: 700;
    font-size: 25px;
    letter-spacing: 1px;
    padding: 0 6px 6px;
    border-bottom: 2px solid var(--copper);
  }
  .label__fact--volume { left: 232px; }
  .label__fact--abv { left: 636px; }
</style>
</head>
<body>
  <section class="label" aria-label="Whisky-Etikett Talwinkel Obermatt">
    <svg class="label__frame" width="1000" height="1064" viewBox="0 0 1000 1064" aria-hidden="true">
      <defs>
        <linearGradient id="copperLine" x1="0" y1="0" x2="1" y2="1">
          <stop offset="0" stop-color="#8a5430"/>
          <stop offset="0.5" stop-color="#d69a68"/>
          <stop offset="1" stop-color="#8a5430"/>
        </linearGradient>
      </defs>
      <polygon points="115,35 885,35 965,115 965,949 885,1029 115,1029 35,949 35,115"
               fill="none" stroke="url(#copperLine)" stroke-width="3"/>
    </svg>

    <div class="label__distillery">BRENNEREI BRUNNACHER</div>
    <div class="label__brand"><span class="label__brand-square"></span><span>Brunnacher</span></div>

    <h1 class="label__name">TALWINKEL</h1>
    <div class="label__subname">Obermatt</div>
    <div class="label__kind">Single Malt Whisky</div>

    <div class="label__producer">Kelvor GmbH</div>
    <div class="label__web">www.kornfaesser.ch</div>
    <div class="label__fact label__fact--volume">50 CL</div>
    <div class="label__fact label__fact--abv">40% VOL</div>
  </section>
</body>
</html>
```